Flyer / Small Safety "Poster" (A4 or 8.5x11" paper)

We're looking to create a series of safety signs for woodworkers to print on home printers using standard sized paper (A4 or 8.5x11" depending on where they are), or possibly to have printed on 17x22" paper.
Currently we want only the first one, but keep in mind that all should work together.
They need: Simple graphic. Bold Text. Company logo. Use company colors (orange, black, white.)
To begin, we will start with a single sign for hearing protection. Graphic or clip art to portray either ear plugs or ear-muff design. Text to say, "Hearing Protection is a Sound Investment."

Target Market(s)

USA Woodworkers & CNC Machinists - Male, 20-65 years old

Font styles to use
Sans Serif

Colors
f37122

Requirements
Must have
• Client logo
Nice to have
• Use client colors of black, white, & orange

```html
<!DOCTYPE html>
<html lang="en">
<head>
<meta charset="utf-8">
<title>Hearing Protection Safety Poster</title>
<link rel="stylesheet" href="https://fonts.googleapis.com/css2?family=Anton&family=PT+Sans:ital,wght@1,400&display=swap">
<style>
  :root {
    --orange: #f37122;
    --orange-light: #f58a38;
    --orange-dark: #de5f0a;
    --black: #231f20;
    --white: #ffffff;
    --stage: #d9d9d9;
  }
  html, body {
    margin: 0;
    padding: 0;
    width: 959px;
    height: 1200px;
    overflow: hidden;
    background: var(--stage);
  }
  .poster {
    position: absolute;
    left: 55px;
    top: 0;
    width: 849px;
    height: 1200px;
    display: block;
  }
  .headline {
    font-family: "Anton", sans-serif;
    paint-order: stroke;
    stroke: var(--orange-dark);
    stroke-width: 5px;
    stroke-linejoin: round;
  }
  .headline--dark { fill: var(--black); }
  .headline--light { fill: var(--white); }
  .safety-label {
    font-family: "Anton", sans-serif;
    fill: var(--black);
  }
  .brand-name {
    font-family: "Anton", sans-serif;
    fill: var(--black);
  }
  .tagline {
    font-family: "PT Sans", sans-serif;
    font-style: italic;
    fill: var(--black);
  }
</style>
</head>
<body>
<svg class="poster" viewBox="0 0 849 1200" xmlns="http://www.w3.org/2000/svg" aria-label="Hearing protection safety poster">
  <defs>
    <radialGradient id="field-glow" cx="50%" cy="45%" r="65%">
      <stop offset="0%" stop-color="var(--orange-light)"/>
      <stop offset="70%" stop-color="var(--orange)"/>
      <stop offset="100%" stop-color="var(--orange-dark)"/>
    </radialGradient>
    <radialGradient id="hover-shadow" cx="50%" cy="50%" r="50%">
      <stop offset="0%" stop-color="#a4440a" stop-opacity="0.75"/>
      <stop offset="100%" stop-color="#a4440a" stop-opacity="0"/>
    </radialGradient>
    <linearGradient id="muff-tone" x1="0" y1="0" x2="0" y2="1">
      <stop offset="0%" stop-color="#2b2627"/>
      <stop offset="40%" stop-color="#f4f1ee"/>
      <stop offset="100%" stop-color="#ffffff"/>
    </linearGradient>
    <pattern id="hazard" width="22" height="40" patternUnits="userSpaceOnUse" patternTransform="skewX(-35)">
      <rect width="22" height="40" fill="var(--orange)"/>
      <rect width="11" height="40" fill="var(--black)"/>
    </pattern>
  </defs>

  <rect class="poster-field" x="0" y="0" width="849" height="1019" fill="url(#field-glow)"/>

  <g class="earmuff-graphic">
    <rect role="img" aria-label="Illustration: left ear-muff cup with headband" x="175" y="0" width="162" height="354" rx="14" fill="url(#muff-tone)"/>
    <rect role="img" aria-label="Illustration: right ear-muff cup with headband" x="511" y="0" width="163" height="354" rx="14" fill="url(#muff-tone)"/>
    <text class="safety-label" transform="translate(462 346) rotate(-90)" font-size="56" textLength="224" lengthAdjust="spacingAndGlyphs">SAFETY</text>
  </g>

  <ellipse class="hover-shadow" cx="421" cy="412" rx="150" ry="12" fill="url(#hover-shadow)"/>

  <g class="headline-stack">
    <text class="headline headline--dark" x="167" y="579" font-size="150" textLength="515" lengthAdjust="spacingAndGlyphs">HEARING</text>
    <text class="headline headline--light" x="167" y="682" font-size="108" textLength="518" lengthAdjust="spacingAndGlyphs">PROTECTION</text>
    <text class="headline headline--dark" transform="translate(235 824) rotate(-90)" font-size="78" textLength="127" lengthAdjust="spacingAndGlyphs">IS A</text>
    <text class="headline headline--dark" x="255" y="826" font-size="157" textLength="424" lengthAdjust="spacingAndGlyphs">SOUND</text>
    <text class="headline headline--light" x="170" y="923" font-size="100" textLength="507" lengthAdjust="spacingAndGlyphs">INVESTMENT</text>
  </g>

  <rect class="hazard-band" x="0" y="978" width="849" height="41" fill="url(#hazard)"/>

  <rect class="footer-panel" x="0" y="1019" width="849" height="181" fill="var(--white)"/>

  <g class="brand-lockup">
    <rect x="126" y="1072" width="44" height="44" fill="var(--orange)"/>
    <text class="brand-name" x="186" y="1116" font-size="52" textLength="562" lengthAdjust="spacingAndGlyphs">CUTLINE SUPPLY</text>
    <text class="tagline" x="748" y="1164" font-size="22" text-anchor="end">Sharp tooling for every shop and every machine.</text>
  </g>
</svg>
</body>
</html>
```